Website Layout for Upcoming Crowdfunding ICO - Digital Currency

We need our website redesigned in a responsive format. Must be attractive with countdown timer to launch, video embedded, PDF whitepaper link, roadmap, team section and contact form. Current website on www.valdrexo.io Experience in previous ICO website designs a plus

Websites that stand out
https://lumivertoken.com/
https://greyfinchledger.com/
http://ico.vantoquelix.com/
https://www.tokvaro.io/

Target Market(s)

Bitcoin Investors
Traders
Forex traders
a public blockchain Traders
ICO investors

Industry/Entity Type

Digital

Coding

Coded - Design and coding required

Number of Pages Required

1 page

Font styles to use
Sans Serif

Colors

Designer to choose colors to be used in the design.

Requirements
Must have
• countdown timer to launch, video embedded, PDF whitepaper link, roadmap, team section and contact form sections
Should not have
• Soft colors

```html
<!DOCTYPE html>
<html lang="en">
<head>
<meta charset="utf-8">
<title>Valdrexo – Asset Backed Property on the Blockchain</title>
<link rel="stylesheet" href="https://fonts.googleapis.com/css2?family=Raleway:wght@400;500;600;700;800&display=swap">
<style>
:root{
  --navy:#0d1a6e;
  --royal:#1f3fd6;
  --blue:#2a6ff0;
  --sky:#3fa3e6;
  --teal:#1fb2cf;
  --purple:#4a1c7e;
  --magenta:#8a1a5c;
  --ink:#1b1b2b;
  --grey:#555a66;
  --line:#d9dce3;
  --foot:#6d6f75;
  --white:#ffffff;
}
*{box-sizing:border-box;margin:0;padding:0}
html,body{width:1200px;height:5200px;overflow:hidden}
body{font-family:"Raleway",sans-serif;color:var(--ink);background:var(--white);position:relative}
.abs{position:absolute}
h2.section-title{font-size:40px;font-weight:700;text-align:center;color:var(--ink)}
.rule{width:90px;height:4px;background:var(--blue);margin:14px auto 0}
.lede{font-size:13px;font-weight:600;text-align:center;color:var(--ink);line-height:1.5;text-transform:uppercase}

/* hero */
.hero{left:0;top:0;width:1200px;height:940px;background:linear-gradient(115deg,#1733b8 0%,#1c2a9a 35%,#3a1d82 70%,#7a1a5e 100%)}
.hero-photo{left:0;top:0;width:1200px;height:560px;background:linear-gradient(160deg,rgba(60,110,230,.55),rgba(20,30,120,.2) 55%,rgba(130,30,90,.45))}
.brand{left:28px;top:26px;display:flex;align-items:center;gap:10px;color:var(--white);font-weight:700;font-size:18px}
.brand-dot{width:34px;height:34px;border-radius:50%;background:#e8a93a}
.nav{right:40px;top:44px;display:flex;gap:26px;font-size:15px;font-weight:700;color:var(--white);text-transform:uppercase}
.nav .flag{width:26px;height:16px;background:#c9d4ee}
.hero-title{left:0;width:1200px;top:250px;text-align:center;color:var(--white);font-size:84px;font-weight:700}
.hero-sub{left:0;width:1200px;top:390px;text-align:center;color:var(--white);font-size:26px;font-weight:500;line-height:1.5}
.count-title{left:0;width:1200px;top:590px;text-align:center;color:var(--white);font-size:34px;font-weight:800}
.count-sub{left:0;width:1200px;top:640px;text-align:center;color:var(--white);font-size:12px;font-weight:700}
.timer{left:440px;top:668px;width:420px;height:96px;background:var(--blue);border-radius:10px;box-shadow:0 6px 22px rgba(0,0,0,.3);display:flex;justify-content:center;align-items:center;gap:8px;color:var(--white)}
.timer .unit{text-align:center;width:76px}
.timer .num{font-size:50px;font-weight:500;line-height:1}
.timer .lbl{font-size:10px;font-weight:600;margin-top:4px}
.timer .sep{font-size:44px;margin-top:-18px}
.hero-wave{left:0;top:780px}

/* business model */
.model{left:0;top:980px;width:1200px}
.model .lede{width:640px;margin:26px auto 0}
.features{left:240px;top:1170px;width:720px;display:grid;grid-template-columns:repeat(3,240px);row-gap:60px}
.feature{text-align:center;padding:0 20px}
.feature svg{height:54px}
.feature h3{font-size:18px;font-weight:700;margin:12px 0 8px}
.feature p{font-size:11px;line-height:1.5;color:var(--grey)}

/* explained */
.explained{left:0;top:1680px;width:1200px;height:320px;background:linear-gradient(180deg,#2c62b8,#3f86d6 60%,#5a9fe0)}
.explained-title{left:0;width:1200px;top:1730px;text-align:center;color:var(--white);font-size:24px;font-weight:800}
.rule-w{left:560px;top:1768px;width:80px;height:3px;background:var(--white)}
.video{top:1800px;width:280px;height:160px;background:var(--white);border-radius:8px;box-shadow:0 4px 16px rgba(0,0,0,.25);display:flex;align-items:center;justify-content:center}

/* whitepaper */
.whitepaper{left:0;width:1200px;top:2080px;text-align:center}
.whitepaper h2{font-size:30px;font-weight:700}
.whitepaper p{font-size:13px;margin-top:22px}
.btn{display:inline-block;margin-top:16px;background:var(--royal);color:var(--white);font-size:14px;font-weight:700;padding:10px 46px;border-radius:22px;text-transform:uppercase}

/* why invest */
.why{left:0;width:1200px;top:2280px}
.why-cols{left:250px;top:2380px;width:700px;display:grid;grid-template-columns:1fr 1fr;gap:40px}
.why-cols h4{font-size:11px;font-weight:800;text-align:center;text-transform:uppercase;margin-bottom:8px}
.why-cols p{font-size:12px;line-height:1.55;color:var(--grey);text-align:justify}
.contract{left:420px;top:2530px;width:360px;height:100px;background:#2f7fd4;color:var(--white);text-align:center;padding-top:20px;z-index:2}
.contract h4{font-size:18px;font-weight:700}
.contract p{font-size:9px;font-weight:700;margin-top:6px;text-transform:uppercase}

/* participate */
.participate{left:0;top:2640px;width:1200px;height:330px;background:linear-gradient(100deg,#2b6fc4,#2a95d4 50%,#1fb8cf)}
.participate-title{left:0;width:1200px;top:2680px;text-align:center;color:var(--white);font-size:40px;font-weight:700}
.participate-sub{left:0;width:1200px;top:2732px;text-align:center;color:var(--white);font-size:11px;font-weight:700;text-transform:uppercase}
.steps{left:220px;top:2790px;width:760px;display:grid;grid-template-columns:repeat(3,1fr);gap:40px;color:var(--white)}
.steps h4{font-size:18px;font-weight:700;text-align:center;margin-bottom:12px}
.steps p{font-size:11px;line-height:1.55;text-align:center}

/* roadmap */
.roadmap{left:0;width:1200px;top:3080px}
.roadmap .lede{margin-top:16px;font-size:11px}
.milestone{left:310px;width:620px;display:flex;align-items:center}
.milestone .badge{width:76px;height:76px;border-radius:50%;background:#2a5d80;display:flex;align-items:center;justify-content:center;color:var(--white);font-weight:800;font-size:22px;flex:none}
.milestone .when{width:230px;padding-left:20px}
.milestone .when b{display:block;font-size:14px;font-weight:800}
.milestone .when span{font-size:14px}
.milestone p{font-size:11px;line-height:1.5;color:var(--grey);width:300px}

/* team */
.team-bg{left:0;top:3980px;width:1200px;height:820px}
.team{left:0;width:1200px;top:3680px}
.team .lede{margin-top:18px;font-size:11px;text-transform:none}
.team-grid{left:240px;top:3800px;width:740px;display:grid;grid-template-columns:repeat(4,175px);gap:18px 12px}
.member{height:170px;background:linear-gradient(160deg,#9aa3b5,#5b6275);position:relative}
.member.lead{background:linear-gradient(180deg,#3a3f52,#1f2333)}
.member .name{position:absolute;left:0;right:0;top:18px;text-align:center;color:var(--white);font-size:14px;font-weight:700}
.member .role{position:absolute;left:0;right:0;top:38px;text-align:center;color:var(--white);font-size:10px}
.member .more{position:absolute;left:0;right:0;top:110px;text-align:center;color:var(--white);font-size:12px;font-weight:700}

/* faq */
.faq-title{left:120px;top:4240px;color:var(--white);font-size:24px;font-weight:700}
.faq{left:240px;top:4290px;width:720px;color:var(--white)}
.faq .q{display:flex;justify-content:space-between;font-size:11px;font-weight:700;padding:8px 0;border-bottom:1px solid rgba(255,255,255,.35)}
.faq .a{font-size:11px;padding:6px 0 10px;font-weight:600}
.faq .chev{font-size:12px}

/* contact */
.contact{left:0;width:1200px;top:4510px;text-align:center;color:var(--white)}
.contact h2{font-size:34px;font-weight:700}
.contact p{font-size:10px;margin-top:6px}
.form{left:320px;top:4590px;width:560px;color:var(--white);font-size:13px}
.field{position:absolute;border-bottom:1px solid rgba(255,255,255,.6);padding-bottom:6px}
.send{position:absolute;left:330px;top:162px;width:140px;height:28px;border:1px solid var(--white);border-radius:16px;text-align:center;line-height:26px;font-size:12px;font-weight:700}

/* footer */
.footer-col{top:4880px}
.footer-col h5{font-size:18px;font-weight:700;margin-bottom:10px}
.footer-col .sub-rule{width:44px;height:3px;background:var(--blue);margin-bottom:14px}
.footer-col li{list-style:none;font-size:12px;line-height:2}
.newsbox{width:230px;height:30px;border:1px solid var(--line);font-size:11px;padding:8px;color:#999}
.subscribe{margin-top:10px;width:110px;height:28px;background:var(--purple);color:var(--white);font-size:11px;font-weight:700;text-align:center;line-height:28px}
.socials{left:490px;top:5070px;display:flex;gap:22px}
.socials span{width:26px;height:26px;background:#8d9098;border-radius:4px}
.bottom-bar{left:0;top:5145px;width:1200px;height:55px;background:var(--foot);color:var(--white);display:flex;align-items:center;justify-content:center;gap:70px;font-size:12px}
.bottom-bar .mark{display:flex;align-items:center;gap:8px;font-weight:700}
.bottom-bar .mark i{width:20px;height:20px;border-radius:50%;background:#e8a93a;display:block}
</style>
</head>
<body>

<!-- hero -->
<div class="abs hero"></div>
<div class="abs hero-photo" role="img" aria-label="Blue-tinted glass building photograph"></div>
<div class="abs brand"><span class="brand-dot"></span>Valdrexo</div>
<nav class="abs nav"><span>Video</span><span>Crowdsale</span><span>Whitepaper</span><span>Join our ICO</span><span>Team</span><span>About</span><span>FAQ</span><span>Contact</span><span class="flag"></span></nav>
<h1 class="abs hero-title">Valdrexo</h1>
<p class="abs hero-sub">ASSET BACKED PROPERTY<br>ON THE BLOCKCHAIN</p>
<h2 class="abs count-title">COUNTDOWN TO CROWDSALE</h2>
<p class="abs count-sub">CROWDSALE STARTS 13 NOVEMBER 2017</p>
<div class="abs timer">
  <div class="unit"><div class="num">37</div><div class="lbl">Days</div></div><div class="sep">:</div>
  <div class="unit"><div class="num">20</div><div class="lbl">Hours</div></div><div class="sep">:</div>
  <div class="unit"><div class="num">15</div><div class="lbl">Minutes</div></div><div class="sep">:</div>
  <div class="unit"><div class="num">49</div><div class="lbl">Seconds</div></div>
</div>
<svg class="abs hero-wave" width="1200" height="170" viewBox="0 0 1200 170"><path d="M0 170 L0 150 C300 150 700 120 1200 0 L1200 170 Z" fill="#fff"/></svg>

<!-- business model -->
<section class="abs model">
  <h2 class="section-title">OUR BUSINESS MODEL</h2><div class="rule"></div>
  <p class="lede">Our clear cut business model on how we're providing value for investors and plans to continue adding value to the token long after the crowdsale closes.</p>
</section>
<div class="abs features">
  <div class="feature"><svg viewBox="0 0 40 54" width="40"><text x="20" y="46" text-anchor="middle" font-family="Raleway,sans-serif" font-weight="800" font-size="52" fill="#1f3fd6">$</text></svg><h3>Raise Funds</h3><p>Our crowdsale will aim to raise $35 million over a period of one month and a day.</p></div>
  <div class="feature"><svg viewBox="0 0 70 54" width="70"><g fill="#1f3fd6"><circle cx="35" cy="14" r="9"/><path d="M20 50c0-14 30-14 30 0z"/><circle cx="13" cy="20" r="7"/><path d="M1 50c0-12 24-12 24 0z"/><circle cx="57" cy="20" r="7"/><path d="M45 50c0-12 24-12 24 0z"/></g></svg><h3>Setup our Team</h3><p>Using the funds raised we will grow our team to find and manage the right buildings.</p></div>
  <div class="feature"><svg viewBox="0 0 54 54" width="54"><path d="M27 4 L50 26 H43 V50 H11 V26 H4 Z" fill="#1f3fd6"/><rect x="22" y="34" width="10" height="16" fill="#fff"/></svg><h3>Buy Property</h3><p>Our team will search for good property investments and carry out due diligence before any purchase.</p></div>
  <div class="feature"><svg viewBox="0 0 60 54" width="60"><rect x="3" y="6" width="54" height="40" rx="3" fill="#1f3fd6"/><rect x="8" y="14" width="44" height="27" fill="#fff"/><rect x="12" y="19" width="16" height="4" fill="#1f3fd6"/><rect x="12" y="27" width="30" height="4" fill="#1f3fd6"/></svg><h3>Develop Investor Platform</h3><p>Token holders can use our investor platform to track their tokens and the properties linked to the portfolio.</p></div>
  <div class="feature"><svg viewBox="0 0 60 54" width="60"><rect x="4" y="20" width="36" height="22" fill="#1f3fd6"/><rect x="20" y="10" width="36" height="22" fill="#3fa3e6"/><circle cx="38" cy="21" r="6" fill="#fff"/></svg><h3>Funds Administration System</h3><p>Profit earned on each ether return is paid back to the holders in line with their holding of the token.</p></div>
  <div class="feature"><svg viewBox="0 0 60 54" width="60"><g fill="#1f3fd6"><rect x="4" y="14" width="40" height="6"/><path d="M44 8 L56 17 L44 26Z"/><rect x="16" y="34" width="40" height="6"/><path d="M16 28 L4 37 L16 46Z"/></g></svg><h3>Trading on the Exchanges</h3><p>Our tokens will be listed on the major crypto exchanges with high trading volumes.</p></div>
</div>

<!-- explained -->
<div class="abs explained" role="img" aria-label="City skyline photograph tinted blue"></div>
<h2 class="abs explained-title">VALDREXO EXPLAINED</h2>
<div class="abs rule-w"></div>
<div class="abs video" style="left:280px"><svg width="44" height="44" viewBox="0 0 44 44"><circle cx="22" cy="22" r="22" fill="#1f3fd6"/><path d="M17 13 L32 22 L17 31Z" fill="#fff"/></svg></div>
<div class="abs video" style="left:632px"><svg width="44" height="44" viewBox="0 0 44 44"><circle cx="22" cy="22" r="22" fill="#1f3fd6"/><path d="M17 13 L32 22 L17 31Z" fill="#fff"/></svg></div>

<!-- whitepaper -->
<section class="abs whitepaper">
  <h2>Whitepaper</h2><div class="rule"></div>
  <p>Our Whitepaper can be viewed below</p>
  <span class="btn">Download here</span>
</section>

<!-- why invest -->
<section class="abs why"><h2 class="section-title">Why Invest in our ICO?</h2><div class="rule"></div></section>
<div class="abs why-cols">
  <div><h4>Tangible asset backs the coin</h4><p>Property provides good annual returns of between 6 – 10% depending on location. Property is relatively stable within the wider market and the risk of large fluctuations in value is low. The capital investment appreciates over the long run and does so consistently.</p></div>
  <div><h4>Coin value is important to us</h4><p>The greatest trend with crypto currency coins is that they change their price and value every day. The fund is structured in a way that the coin is only as volatile as its property portfolio, which means we can see big profits and growth from the company itself over time.</p></div>
</div>
<div class="abs contract"><h4>CONTRACT ADDRESS</h4><p>Contract address will be<br>published here on the launch</p></div>

<!-- participate -->
<div class="abs participate"></div>
<h2 class="abs participate-title">HOW DO I PARTICIPATE?</h2>
<p class="abs participate-sub">How to invest in the Valdrexo initial coin offering (ICO)</p>
<div class="abs steps">
  <div><h4>Buy Ether</h4><p>Signup for a crypto wallet, then buy ether through an exchange or an online service. Keep your ether in the wallet until the sale starts.</p></div>
  <div><h4>Transfer Ether</h4><p>Once you have successfully purchased your ether, ensure that you send the amount of ether you wish to invest to the crowdsale contract address shown.</p></div>
  <div><h4>Receive Tokens</h4><p>The tokens will be sent to your wallet address once the transfer is confirmed. They will then appear in your account and are ready to trade on listed exchanges.</p></div>
</div>

<!-- roadmap -->
<section class="abs roadmap"><h2 class="section-title">ROADMAP</h2><div class="rule"></div><p class="lede">Timeline of events leading up to our ICO</p></section>
<div class="abs milestone" style="top:3170px"><div class="badge"><svg width="34" height="34" viewBox="0 0 34 34"><circle cx="17" cy="17" r="14" fill="none" stroke="#fff" stroke-width="3"/><path d="M17 9v9l6 4" stroke="#fff" stroke-width="3" fill="none"/></svg></div><div class="when"><b>JUNE 2017</b><span>Our Beginnings</span></div><p>Founders came together to plan how to purchase properties throughout the world and create a portfolio to back the Valdrexo token.</p></div>
<div class="abs milestone" style="top:3290px"><div class="badge">ICO</div><div class="when"><b>JULY 2017</b><span>An ICO is born</span></div><p>The founders choose a public blockchain to bring a token to market, thus the Valdrexo token was born.</p></div>
<div class="abs milestone" style="top:3410px"><div class="badge"><svg width="40" height="34" viewBox="0 0 40 34"><g fill="#fff"><circle cx="20" cy="9" r="6"/><path d="M10 32c0-12 20-12 20 0z"/><circle cx="7" cy="13" r="4"/><circle cx="33" cy="13" r="4"/></g></svg></div><div class="when"><b>NOVEMBER 2017</b><span>Gather Investors</span></div><p>Through our detailed and transparent whitepaper which outlines our goals for building up the property portfolio we rally investors.</p></div>
<div class="abs milestone" style="top:3540px"><div class="badge">P</div><div class="when"><b>JANUARY 2018</b><span>Transition to Full Service</span></div><p>Once the crowdsale period for the token closes the funds will be listed on the crypto exchanges and carry out the business plan as detailed in the whitepaper.</p></div>

<!-- team -->
<svg class="abs team-bg" width="1200" height="820" viewBox="0 0 1200 820" role="presentation">
  <defs><linearGradient id="teamGrad" x1="0" y1="0" x2="1" y2="1"><stop offset="0" stop-color="#1b2fa8"/><stop offset=".55" stop-color="#2a2a8e"/><stop offset="1" stop-color="#5a1f78"/></linearGradient></defs>
  <path d="M0 60 C400 140 800 0 1200 30 L1200 820 L0 820 Z" fill="url(#teamGrad)"/>
</svg>
<section class="abs team"><h2 class="section-title">Our Amazing Team</h2><div class="rule"></div><p class="lede">The key people behind the Valdrexo token and ICO launch</p></section>
<div class="abs team-grid">
  <div class="member lead" role="img" aria-label="Team member portrait"><div class="name">Dane Holloway</div><div class="role">CEO / Founder</div><div class="more">Read more</div></div>
  <div class="member" role="img" aria-label="Team member portrait"></div>
  <div class="member" role="img" aria-label="Team member portrait"></div>
  <div class="member" role="img" aria-label="Team member portrait"></div>
  <div class="member" role="img" aria-label="Team member portrait"></div>
  <div class="member" role="img" aria-label="Team member portrait"></div>
  <div class="member" role="img" aria-label="Team member portrait"></div>
  <div class="member" role="img" aria-label="Team member portrait"></div>
</div>

<!-- faq -->
<h2 class="abs faq-title">FREQUENTLY ASKED QUESTIONS</h2>
<div class="abs faq">
  <div class="q"><span>When does the crowdsale start?</span><span class="chev">▾</span></div>
  <div class="a">Our crowdsale starts officially on the 13 November 2017 with the first day being our largest bonus day.</div>
  <div class="q"><span>What does your token give me?</span><span class="chev">▾</span></div>
  <div class="q"><span>Do you have a capped crowdsale?</span><span class="chev">▾</span></div>
  <div class="q"><span>What currencies do you accept?</span><span class="chev">▾</span></div>
</div>

<!-- contact -->
<section class="abs contact"><h2>CONTACT US</h2><p>Any questions about investing, send them our way</p></section>
<div class="abs form">
  <div class="field" style="left:0;top:0;width:240px">Name</div>
  <div class="field" style="left:270px;top:0;width:290px;height:110px">Message</div>
  <div class="field" style="left:0;top:56px;width:240px">Email</div>
  <div class="field" style="left:0;top:112px;width:240px">Phone</div>
  <div class="send">SEND</div>
</div>

<!-- footer -->
<div class="abs footer-col" style="left:120px"><h5>Sitemap</h5><div class="sub-rule"></div><ul><li>Video</li><li>Whitepaper</li><li>Join our ICO</li></ul></div>
<div class="abs footer-col" style="left:480px"><h5>About</h5><div class="sub-rule"></div><ul><li>Roadmap</li><li>Team</li><li>FAQ</li></ul></div>
<div class="abs footer-col newsletter" style="left:760px"><h5>Subscribe to our newsletter</h5><div class="sub-rule"></div><div class="newsbox">Your Email</div><div class="subscribe">SUBSCRIBE</div></div>
<div class="abs socials"><span></span><span></span><span></span><span></span><span></span><span></span></div>
<div class="abs bottom-bar"><span>Copyright © Valdrexo 2017</span><span class="mark"><i></i>Valdrexo</span><span>Privacy Policy &nbsp; | &nbsp; Terms of Use</span></div>

</body>
</html>
```